BrightKeel Business Card Contest

We are looking for a modern business card that catches attention and is unique. Attached is the brand guide and logo files. Please note that the back side (not the side with our name and info) with be UV raise printed, so have fun with the design there. We want to include Name, Title, Phone number, email, website.

Contact Information for Business Card

Please see project description

```html
<!DOCTYPE html>
<html lang="en">
<head>
<meta charset="utf-8">
<title>BrightKeel Business Card</title>
<link rel="stylesheet" href="https://fonts.googleapis.com/css2?family=Outfit:wght@400;500;600;700&display=swap">
<style>
  :root {
    --stage: #0f0f0f;
    --paper: #ffffff;
    --ink: #1c1c22;
    --ink-soft: #2e2e36;
    --navy: #0b3270;
    --royal: #0c4fa0;
    --azure: #1e7ecf;
    --cyan: #19c0e4;
    --red: #d92e21;
    --orange: #ee7d1c;
  }
  * { box-sizing: border-box; margin: 0; padding: 0; }
  html, body {
    width: 1200px; height: 1200px; overflow: hidden;
    background: var(--stage);
    font-family: "Outfit", sans-serif;
  }
  .card {
    position: absolute;
    left: 237px;
    width: 729px;
    height: 416px;
    border-radius: 32px;
    overflow: hidden;
  }
  .card-front { top: 137px; background: var(--paper); color: var(--ink); }
  .card-back { top: 622px; }

  .brand {
    position: absolute; left: 46px; top: 46px;
    display: flex; flex-direction: column; align-items: flex-start; gap: 10px;
  }
  .brand-square { width: 30px; height: 30px; background: var(--ink); margin-left: 80px; }
  .brand-name { font-size: 50px; font-weight: 500; letter-spacing: -0.5px; line-height: 1; color: var(--ink); }

  .person {
    position: absolute; right: 49px; top: 212px; text-align: right;
  }
  .person-name { font-size: 29px; font-weight: 700; line-height: 1.05; letter-spacing: 0.2px; }
  .person-title { font-size: 20px; font-weight: 500; color: var(--ink-soft); margin-top: 2px; }

  .divider {
    position: absolute; left: 46px; top: 280px; width: 638px; height: 3px; border-radius: 2px;
    background: linear-gradient(90deg, var(--royal), var(--cyan) 20%, #7fa08a 45%, var(--orange) 70%, var(--red));
  }

  .contacts {
    position: absolute; left: 46px; top: 296px; list-style: none;
  }
  .contacts li {
    display: flex; align-items: center; height: 26px;
    font-size: 20px; font-weight: 500; color: var(--ink);
  }
  .contacts svg { width: 18px; height: 18px; margin-right: 13px; flex: none; }

  .back-art {
    position: absolute; inset: 0;
    background: linear-gradient(225deg, var(--azure) 0%, var(--navy) 40%, var(--red) 68%, var(--orange) 100%);
  }
  .back-brand {
    position: absolute; left: 50%; top: 50%; transform: translate(-50%, -50%);
    font-size: 42px; font-weight: 600; color: var(--paper); letter-spacing: -0.3px; white-space: nowrap;
  }
</style>
</head>
<body>

<section class="card card-front" aria-label="Business card front">
  <div class="brand">
    <span class="brand-square"></span>
    <span class="brand-name">BrightKeel</span>
  </div>

  <div class="person">
    <div class="person-name">NOLAN HARWICK</div>
    <div class="person-title">Founder &amp; CEO</div>
  </div>

  <div class="divider"></div>

  <ul class="contacts">
    <li>
      <svg viewBox="0 0 24 24" fill="none" stroke="currentColor" stroke-width="2" stroke-linecap="round" stroke-linejoin="round"><path d="M5 3h4l2 5-3 2a11 11 0 0 0 6 6l2-3 5 2v4a2 2 0 0 1-2 2A17 17 0 0 1 3 5a2 2 0 0 1 2-2z"/><path d="M15 3a6 6 0 0 1 6 6"/><path d="M15 7a2 2 0 0 1 2 2"/></svg>
      (555) 014-2738
    </li>
    <li>
      <svg viewBox="0 0 24 24" fill="none" stroke="currentColor" stroke-width="1.4" stroke-linejoin="round"><rect x="2" y="5" width="20" height="14" rx="1"/><path d="M2 6l10 7 10-7"/></svg>
      info@brightkeel.com
    </li>
    <li>
      <svg viewBox="0 0 24 24" fill="none" stroke="currentColor" stroke-width="1.3"><circle cx="12" cy="12" r="10"/><ellipse cx="12" cy="12" rx="4.5" ry="10"/><path d="M2 12h20M12 2v20M4 7h16M4 17h16"/></svg>
      brightkeel.com
    </li>
  </ul>
</section>

<section class="card card-back" aria-label="Business card back">
  <div class="back-art" role="img" aria-label="Decorative artwork in blue, red and orange tones, printed with raised UV finish"></div>
  <div class="back-brand">BrightKeel</div>
</section>

</body>
</html>
```